Luxury Caviar Tin Label for High End Caviar Retailer

We are looking for a new caviar label design. We want something unique, preferably black and gold or dark blue and gold. We want a modern and luxurious feel. We have several types of caviar so we need to be able to change the name of the caviar when we print the labels. See inspiration attached. Logo is also attached. More about us: velmoronfare.com

Industry/Entity Type

fine foods industry, caviar

Font styles to use
Serif
Decorative

Requirements
Must have
• KT Velmoron Logo, space for caviar name
Nice to have
• black and gold, blue and gold

```html
<!DOCTYPE html>
<html lang="en">
<head>
<meta charset="utf-8">
<title>KT Velmoron Caviar – Royal Siberian Tin Label</title>
<link rel="stylesheet" href="https://fonts.googleapis.com/css2?family=Cinzel:wght@400;500&family=Great+Vibes&family=Marcellus&family=Source+Serif+4:wght@400&display=swap">
<style>
  :root {
    --page: #ffffff;
    --tin-black: #060708;
    --pattern-dark: #0b0c0d;
    --pattern-light: #17171a;
    --gold: #e0a83a;
  }
  html, body {
    margin: 0;
    padding: 0;
    width: 1200px;
    height: 1000px;
    overflow: hidden;
    background: var(--page);
  }
  .label-canvas {
    display: block;
    width: 1200px;
    height: 1000px;
  }
  .tin-disc { fill: var(--tin-black); }
  .gold-ring { fill: none; stroke: var(--gold); }
  .gold-ring--outer { stroke-width: 2; }
  .gold-ring--inner { stroke-width: 2.5; }
  .brand-mark { fill: none; stroke: var(--gold); stroke-width: 2; }
  .brand-name {
    font-family: "Marcellus", serif;
    font-size: 34px;
    fill: var(--gold);
    letter-spacing: 1px;
  }
  .product-word {
    font-family: "Cinzel", serif;
    font-weight: 500;
    font-size: 54px;
    fill: var(--gold);
  }
  .variety-name {
    font-family: "Great Vibes", cursive;
    font-size: 92px;
    fill: var(--gold);
  }
  .rim-text {
    font-family: "Source Serif 4", serif;
    font-size: 20px;
    letter-spacing: 2.2px;
    fill: var(--gold);
  }
</style>
</head>
<body>
<svg class="label-canvas" viewBox="0 0 1200 1000" xmlns="http://www.w3.org/2000/svg">
  <defs>
    <radialGradient id="patternTone" cx="50%" cy="50%" r="50%">
      <stop offset="0%" stop-color="var(--pattern-light)"/>
      <stop offset="100%" stop-color="var(--pattern-dark)"/>
    </radialGradient>
    <path id="rimPath" d="M 603 144 A 356 356 0 1 0 603 856 A 356 356 0 1 0 603 144"/>
  </defs>

  <g class="tin-label">
    <circle class="tin-disc" cx="603" cy="500" r="389"/>
    <circle class="gold-ring gold-ring--outer" cx="603" cy="500" r="382"/>

    <circle class="honeycomb-field" cx="603" cy="500" r="321" fill="url(#patternTone)"
            role="img" aria-label="Subtle dark honeycomb pattern texture"/>
    <circle class="gold-ring gold-ring--inner" cx="603" cy="500" r="333"/>

    <g class="rim-copy">
      <text class="rim-text rim-text--ingredients">
        <textPath href="#rimPath" startOffset="215">Ingredients: caviar - salt</textPath>
      </text>
      <text class="rim-text rim-text--storage" text-anchor="middle">
        <textPath href="#rimPath" startOffset="1122">Keep refregerated 28 - 34</textPath>
      </text>
      <text class="rim-text rim-text--web">
        <textPath href="#rimPath" startOffset="1680">www.velmoronfare.com</textPath>
      </text>
    </g>

    <g class="brand-block">
      <circle class="brand-mark" cx="603" cy="294" r="56"/>
      <text class="brand-name" x="603" y="415" text-anchor="middle">KT VELMORON</text>
      <text class="product-word" x="604" y="485" text-anchor="middle" textLength="306" lengthAdjust="spacing">CAVIER</text>
    </g>

    <g class="variety-block">
      <text class="variety-name" x="600" y="628" text-anchor="middle">Royal</text>
      <text class="variety-name" x="604" y="720" text-anchor="middle">Siberian</text>
    </g>
  </g>
</svg>
</body>
</html>
```